Webbanner-Design für Ebook - Unterwegs im Süden Ungarns ( Affiliate und Promivo)
Zielgruppe
Wir verkaufen Ebooks. In diesem Fall möchten wir Kroatien Liebhaber aufmerksam machen, dass es mittlerweile ein Buch gibt, welches all die Sehenswürdigkeiten und Routen bis nach Kroatien ausführlich beschreibt.
Aufgabenstellung
Da wir unseren Affiliate Partner die Möglichkeit geben wollen, unsere Produkte zu verkaufen, benötigen wir diesbezüglich gute Anzeigen mit verschiedener Größen. ( affiliate und Promivo )
Sollten Vorlagen / Stockfotos verwendet werden, dann bitte über bildfang
Ich habe einige Fotos welches wir bereits erworben haben hier hochgeladen.
Auch das Coverbild ist im Anhang.
Ideal wäre eine Buch-Abbildung für die Anzeigen.
3 Anzeigegrößen erforderlich
728 x 90 300 x 250 300 x 600

```html
<!DOCTYPE html>
<html lang="de">
<head>
<meta charset="utf-8">
<title>Webbanner – Unterwegs im Süden Ungarns</title>
<link rel="stylesheet" href="https://fonts.googleapis.com/css2?family=Roboto:wght@400;500;700;900&family=Roboto+Condensed:wght@400;700&display=swap">
<style>
  :root {
    --navy: #3a5584;
    --navy-dark: #2f4870;
    --band: #9aaecb;
    --paper: #f3f3f3;
    --paper-edge: #e4e4e4;
    --red: #d8232a;
    --red-dark: #b3161c;
    --stage: #ececec;
    --cover-sky: #6f8fb8;
    --cover-sea: #3f6aa0;
    --cover-town: #c99b6e;
  }
  * { box-sizing: border-box; margin: 0; padding: 0; }
  html, body { width: 1200px; height: 1200px; overflow: hidden; }
  body {
    background: var(--stage);
    font-family: "Roboto", Arial, sans-serif;
    position: relative;
  }
  .banner {
    position: absolute;
    background: var(--paper);
    overflow: hidden;
    box-shadow: 0 4px 12px rgba(0,0,0,.25);
    border: 1px solid var(--paper-edge);
  }
  .banner svg.shape { position: absolute; left: 0; top: 0; }
  .headline {
    position: absolute;
    color: #fff;
    text-align: center;
    text-transform: uppercase;
    line-height: 1.1;
  }
  .headline .light { font-weight: 400; }
  .headline .bold { font-weight: 700; }
  .guide {
    position: absolute;
    font-family: "Roboto Condensed", Arial Narrow, sans-serif;
    color: var(--navy);
    text-transform: uppercase;
    line-height: 1.25;
  }
  .guide b { font-weight: 700; }
  .ebook {
    position: absolute;
    color: var(--red);
    font-weight: 700;
    letter-spacing: .5px;
  }
  .cta {
    position: absolute;
    background: linear-gradient(#e9383e, var(--red) 55%, var(--red-dark));
    color: #fff;
    font-weight: 700;
    letter-spacing: 2px;
    text-align: center;
    outline: 2px solid #fff;
    box-shadow: 0 0 0 3px #cfcfcf;
    text-transform: uppercase;
  }
  .book-cover {
    position: absolute;
    background: linear-gradient(180deg, var(--navy) 0 22%, var(--cover-sky) 22% 45%, var(--cover-town) 45% 68%, var(--cover-sea) 68%);
    box-shadow: 3px 3px 6px rgba(0,0,0,.35), inset -3px 0 0 rgba(255,255,255,.5);
  }

  /* 728 x 90 */
  .leaderboard { left: 298px; top: 236px; width: 624px; height: 77px; }
  .leaderboard .book-cover { left: 28px; top: 4px; width: 44px; height: 68px; }
  .leaderboard .ebook { left: 106px; top: 12px; width: 120px; text-align: center; font-size: 21px; }
  .leaderboard .cta { left: 106px; top: 43px; width: 120px; height: 21px; font-size: 13px; line-height: 21px; }
  .leaderboard .guide { left: 240px; top: 22px; font-size: 14px; }
  .leaderboard .headline { left: 440px; top: 13px; width: 184px; font-size: 16px; }

  /* 300 x 600 */
  .skyscraper { left: 296px; top: 389px; width: 257px; height: 513px; }
  .skyscraper .headline { left: 0; top: 14px; width: 257px; }
  .skyscraper .h1 { font-size: 21px; }
  .skyscraper .h2 { font-size: 23px; margin-top: 4px; }
  .skyscraper .h3 { font-size: 31px; margin-top: 2px; }
  .skyscraper .guide { left: 0; top: 176px; width: 257px; text-align: center; font-size: 17px; }
  .skyscraper .book-cover { left: 88px; top: 246px; width: 78px; height: 120px; }
  .skyscraper .ebook { left: 0; top: 393px; width: 257px; text-align: center; font-size: 40px; }
  .skyscraper .cta { left: 29px; top: 452px; width: 196px; height: 36px; font-size: 22px; line-height: 36px; }

  /* 300 x 250 */
  .rectangle { left: 671px; top: 516px; width: 258px; height: 214px; }
  .rectangle .headline { left: 0; top: 12px; width: 258px; }
  .rectangle .h1 { font-size: 15px; }
  .rectangle .h2 { font-size: 19px; margin-top: 3px; }
  .rectangle .ebook { left: 9px; top: 101px; font-size: 27px; }
  .rectangle .guide { left: 10px; top: 133px; font-size: 13px; }
  .rectangle .cta { left: 9px; top: 172px; width: 136px; height: 25px; font-size: 15px; line-height: 25px; }
  .rectangle .book-cover { left: 166px; top: 88px; width: 76px; height: 118px; }
</style>
</head>
<body>

  <!-- Leaderboard 728 x 90 -->
  <section class="banner leaderboard" aria-label="Banner 728 x 90">
    <svg class="shape" width="624" height="77" viewBox="0 0 624 77">
      <path d="M420 0 L624 0 L624 77 L420 77 L420 49 L406 38 L420 27 Z" fill="var(--band)"/>
      <path d="M428 0 L624 0 L624 77 L428 77 L428 49 L414 38 L428 27 Z" fill="var(--navy)"/>
    </svg>
    <div class="book-cover" role="img" aria-label="Buchcover des Ebooks mit Küstenstadt am Meer"></div>
    <div class="ebook">EBOOK</div>
    <div class="cta">Hier klicken</div>
    <p class="guide">Der perfekte Guide<br>für <b>Fahrer &amp; Beifahrer</b></p>
    <p class="headline"><span class="light">Unterwegs im</span><br><span class="bold">Süden Ungarns?</span></p>
  </section>

  <!-- Skyscraper 300 x 600 -->
  <section class="banner skyscraper" aria-label="Banner 300 x 600">
    <svg class="shape" width="257" height="160" viewBox="0 0 257 160">
      <path d="M0 0 H257 V100 Q200 118 152 122 L128 142 L104 122 Q56 118 0 100 Z" fill="var(--band)"/>
      <path d="M0 0 H257 V90 Q200 108 148 112 L128 130 L108 112 Q56 108 0 90 Z" fill="var(--navy)"/>
    </svg>
    <div class="headline">
      <div class="h1 light">Unterwegs im</div>
      <div class="h2 bold">Süden</div>
      <div class="h3 bold">Ungarns?</div>
    </div>
    <p class="guide">Der perfekte Guide<br>für <b>Fahrer &amp; Beifahrer</b></p>
    <div class="book-cover" role="img" aria-label="Buchcover des Ebooks mit Küstenstadt am Meer"></div>
    <div class="ebook">EBOOK</div>
    <div class="cta">Hier klicken</div>
  </section>

  <!-- Medium Rectangle 300 x 250 -->
  <section class="banner rectangle" aria-label="Banner 300 x 250">
    <svg class="shape" width="258" height="100" viewBox="0 0 258 100">
      <path d="M0 0 H258 V60 Q200 72 138 74 L122 90 L106 74 Q50 70 0 56 Z" fill="var(--band)"/>
      <path d="M0 0 H258 V52 Q200 64 136 66 L122 80 L108 66 Q50 62 0 48 Z" fill="var(--navy)"/>
    </svg>
    <div class="headline">
      <div class="h1 light">Unterwegs im</div>
      <div class="h2 bold">Süden Ungarns?</div>
    </div>
    <div class="ebook">EBOOK</div>
    <p class="guide">Der perfekte Guide<br>für <b>Fahrer &amp; Beifahrer</b></p>
    <div class="cta">Hier klicken</div>
    <div class="book-cover" role="img" aria-label="Buchcover des Ebooks mit Küstenstadt am Meer"></div>
  </section>

</body>
</html>
```